Accounting practice seeks business card redesign with existing logo

Accounting practice has logo and slogan but more needs modern professional business revision. Must be in a file format ready to print quality business cards.

Open to artistic ideas but for the brand recognition the features below must be incorporated:

- Logo: attached in EPS format (Logo now blue)
- Slogan: Proven Business Solutions... That Work! (in orange legible handwriting type font)
- Name: Dorian T Felsham RBA AAT JP (letters in smaller font)
- Phone icon: 1800 593 817
- Mobile phone icon: 0488 614 752
- Web icon: www.velprasolutions.com.au
- Email icon: admin@velprasolutions.com.au
- See pics for dark blue/med blue line at bottom, this is a necessity.
- Globe that forms the 'dot' in the 'I' of Velpra is attached. It is too big at present.
- Rear side: pic attached. Note my logo is a watermark. I Will provide slightly revised wording details later. Please allow for a small white space at bottom of rear of card to write notes/appointment details.

I am open to ideas but must retain the above for brand recognition.

```html
<!DOCTYPE html>
<html lang="en">
<head>
<meta charset="utf-8">
<title>Velpra Solutions – Business Card</title>
<link href="https://fonts.googleapis.com/css2?family=Arimo:wght@400;500;700&family=Kalam:wght@700&display=swap" rel="stylesheet">
<style>
  :root {
    --navy: #1b2956;
    --blue: #0f78be;
    --orange: #f08a1c;
    --ink: #1a1a1a;
    --muted: #444b57;
    --divider: #c9c9c9;
    --paper: #ffffff;
    --white: #ffffff;
  }
  html, body {
    margin: 0;
    padding: 0;
    overflow: hidden;
    background: var(--paper);
  }
  .card {
    position: relative;
    width: 1200px;
    height: 686px;
    overflow: hidden;
    background: var(--paper);
    font-family: "Arimo", Arial, sans-serif;
    color: var(--ink);
  }
  .card-shapes {
    position: absolute;
    inset: 0;
  }
  .shape-navy { fill: var(--navy); }
  .shape-blue { fill: var(--blue); }
  .divider { stroke: var(--divider); stroke-width: 3; }

  .slogan {
    position: absolute;
    left: 150px;
    top: 34px;
    width: 580px;
    margin: 0;
    text-align: center;
    font-family: "Kalam", "Comic Sans MS", cursive;
    font-weight: 700;
    font-size: 34px;
    line-height: 1.1;
    color: var(--orange);
  }
  .tagline {
    position: absolute;
    left: 70px;
    top: 112px;
    width: 740px;
    margin: 0;
    text-align: center;
    font-size: 30px;
    line-height: 41px;
    font-weight: 400;
  }
  .holder {
    position: absolute;
    left: 150px;
    top: 252px;
    width: 790px;
    margin: 0;
    text-align: center;
    font-size: 24px;
    font-weight: 700;
    color: var(--navy);
  }
  .holder-titles {
    font-size: 16px;
    font-weight: 500;
    letter-spacing: 1px;
    margin-left: 6px;
  }
  .contacts {
    position: absolute;
    left: 170px;
    top: 294px;
    width: 760px;
    margin: 0;
    padding: 0;
    list-style: none;
    display: grid;
    grid-template-columns: 290px 1fr;
    row-gap: 12px;
    column-gap: 10px;
    font-size: 18px;
    color: var(--muted);
  }
  .contact {
    display: flex;
    align-items: center;
    gap: 10px;
    white-space: nowrap;
  }
  .contact-icon {
    width: 22px;
    height: 22px;
    flex: none;
    fill: none;
    stroke: var(--blue);
    stroke-width: 2;
    stroke-linecap: round;
    stroke-linejoin: round;
  }
  .service {
    position: absolute;
    margin: 0;
    font-size: 33px;
    line-height: 1;
    white-space: nowrap;
  }
  .brand {
    position: absolute;
    left: 42px;
    top: 586px;
    display: flex;
    align-items: center;
    gap: 12px;
    color: var(--white);
    font-size: 48px;
    font-weight: 400;
    letter-spacing: 2px;
  }
  .brand-dot {
    width: 14px;
    height: 14px;
    border-radius: 50%;
    background: var(--white);
  }
  .base-line {
    position: absolute;
    left: 0;
    bottom: 0;
    width: 100%;
    height: 14px;
    display: flex;
    flex-direction: column;
  }
  .base-line-navy { height: 8px; background: var(--navy); }
  .base-line-blue { height: 6px; background: var(--blue); }
</style>
</head>
<body>
<div class="card">
  <svg class="card-shapes" width="1200" height="686" viewBox="0 0 1200 686" aria-hidden="true">
    <polygon class="shape-navy" points="0,76 330,686 0,686"/>
    <polygon class="shape-blue" points="809,0 1200,0 1200,668"/>
    <line class="divider" x1="556" y1="372" x2="724" y2="620"/>
  </svg>

  <p class="slogan">Proven Business Solutions... That Work!</p>

  <p class="tagline">Your trusted provider of quality business and<br>accounting solutions, proven. to work for<br>small to medium business and tradies.</p>

  <p class="holder">Dorian T Felsham<span class="holder-titles">RBA AAT JP</span></p>

  <ul class="contacts">
    <li class="contact">
      <svg class="contact-icon" viewBox="0 0 24 24" aria-hidden="true"><path d="M5 3h4l2 5-2.5 1.5a11 11 0 0 0 6 6L16 13l5 2v4a2 2 0 0 1-2 2A16 16 0 0 1 3 5a2 2 0 0 1 2-2z"/></svg>
      <span>1800 593 817</span>
    </li>
    <li class="contact">
      <svg class="contact-icon" viewBox="0 0 24 24" aria-hidden="true"><circle cx="12" cy="12" r="9"/><path d="M3 12h18M12 3a14 14 0 0 1 0 18M12 3a14 14 0 0 0 0 18"/></svg>
      <span>www.velprasolutions.com.au</span>
    </li>
    <li class="contact">
      <svg class="contact-icon" viewBox="0 0 24 24" aria-hidden="true"><rect x="6" y="2" width="12" height="20" rx="2"/><path d="M11 18h2"/></svg>
      <span>0488 614 752</span>
    </li>
    <li class="contact">
      <svg class="contact-icon" viewBox="0 0 24 24" aria-hidden="true"><rect x="3" y="5" width="18" height="14" rx="1.5"/><path d="M3 6l9 7 9-7"/></svg>
      <span>admin@velprasolutions.com.au</span>
    </li>
  </ul>

  <p class="service" style="left:223px; top:404px;">Bookkeeping</p>
  <p class="service" style="left:255px; top:450px;">BAS</p>
  <p class="service" style="left:276px; top:496px;">Cloud Accounting</p>
  <p class="service" style="left:298px; top:541px;">Debt Recovery</p>

  <p class="service" style="left:713px; top:404px;">Business Advice</p>
  <p class="service" style="left:754px; top:450px;">ATO Assistance</p>
  <p class="service" style="left:776px; top:496px;">Office Technology</p>
  <p class="service" style="left:808px; top:541px;">And Much More..</p>

  <div class="brand">
    <span class="brand-name">Velpra</span>
    <span class="brand-dot"></span>
  </div>

  <div class="base-line" aria-hidden="true">
    <div class="base-line-navy"></div>
    <div class="base-line-blue"></div>
  </div>
</div>
</body>
</html>
```